Web Design

We need a website for a company based in Doha Qatar called
Velvanta Staffing Co..

It is the number one maid cleaning service company, and we have branches all over qatar.

Luxury Cleaning Service Provider.

The color scheme is gold, yellow and black like the logo.

Before they get to the website, there is an intro video.

The website should depict luxury.

Target Market(s)

People who need maids at their houses.

Industry/Entity Type

Cleaning Service

Requirements
Must have
• Luxury, Sleek, Modern

The opening sequence is a video which I already have. Its too big to upload here so I am going to put it on youtube.

After the opening sequence, the home page should have a widescreen photo background and it should change every five seconds, the first background photo should be of qatar westbay skyline. Then the second background should be of maid photos in cleaning positions. Then the third background should be of cleaner photos etc.

We will send you all the tabs and all the content later.

```html
<!DOCTYPE html>
<html lang="en">
<head>
<meta charset="utf-8">
<title>Velvanta Staffing Co. — Team</title>
<link rel="stylesheet" href="https://fonts.googleapis.com/css2?family=Nunito+Sans:wght@400;600;700;800&display=swap">
<style>
  :root {
    --gold: #d9a21b;
    --gold-light: #f6d35a;
    --gold-dark: #e0ac22;
    --ink: #2b1b0f;
    --brown: #2a1709;
    --brown-deep: #1e0f05;
    --text: #333333;
    --line: #cfcfcf;
    --white: #ffffff;
  }
  * { box-sizing: border-box; margin: 0; padding: 0; }
  html, body { width: 769px; height: 1200px; overflow: hidden; }
  body {
    position: relative;
    background: var(--white);
    font-family: "Nunito Sans", Arial, sans-serif;
    color: var(--text);
  }
  .hero-backdrop {
    position: absolute; left: 0; top: 0; width: 769px; height: 422px;
    background: linear-gradient(180deg, #8d8d8d 0%, #6f6f6f 55%, #4b4b4b 100%);
  }
  .hero-backdrop::before {
    content: ""; position: absolute; left: 0; right: 0; top: 0; height: 3px; background: var(--brown);
  }
  .nav-bar {
    position: absolute; top: 4px; height: 70px; width: 240px;
    background: linear-gradient(180deg, var(--gold-light) 0%, var(--gold-dark) 100%);
    display: flex; align-items: center; justify-content: space-around;
    padding: 0 14px;
    box-shadow: 0 3px 6px rgba(0,0,0,.3);
  }
  .nav-bar--left { left: 76px; }
  .nav-bar--right { left: 452px; }
  .nav-bar a {
    font-size: 9px; font-weight: 700; color: var(--ink); text-decoration: none; letter-spacing: .2px;
  }
  .brand {
    position: absolute; left: 317px; top: 0; width: 135px; height: 108px;
    background: linear-gradient(180deg, #3a2410 0%, var(--brown-deep) 100%);
    display: flex; align-items: center; justify-content: center; text-align: center;
    padding: 0 10px;
  }
  .brand-name {
    font-size: 11px; font-weight: 700; color: var(--gold-light); line-height: 1.3;
  }
  .hero-slide {
    position: absolute; left: 76px; top: 86px; width: 616px; height: 298px;
    background: linear-gradient(90deg, #c9c0b2 0%, #8f8170 35%, #3d3128 60%, #d8d2c8 85%, #6b5c4e 100%);
  }
  .slide-dots {
    position: absolute; left: 348px; top: 360px; display: flex; gap: 5px;
  }
  .slide-dots span {
    width: 10px; height: 10px; border-radius: 50%; background: var(--white);
  }
  .slide-dots span.is-active { background: transparent; border: 1.5px solid var(--gold-light); }

  .section-title {
    position: absolute; left: 0; width: 769px; text-align: center;
    font-size: 12px; font-weight: 800; color: var(--gold); letter-spacing: .3px;
  }
  .team-title { top: 448px; }
  .team-intro {
    position: absolute; left: 78px; top: 480px; width: 613px; text-align: center;
    font-size: 8.6px; line-height: 15.5px; color: var(--text);
  }
  .training-title { top: 561px; }

  .program-card {
    position: absolute; top: 589px; width: 201px; height: 180px;
    border: 1px solid var(--line); background: var(--white);
  }
  .program-card:nth-of-type(1) { left: 77px; }
  .card-a { left: 77px; }
  .card-b { left: 284px; }
  .card-c { left: 490px; }
  .card-head {
    height: 39px; padding: 0 14px; display: flex; align-items: center;
    background: linear-gradient(180deg, var(--gold-light) 0%, var(--gold-dark) 100%);
    font-size: 8.6px; font-weight: 700; color: var(--ink);
  }
  .card-body {
    padding: 9px 14px 0; font-size: 7.2px; line-height: 14px; color: var(--text);
  }
  .card-list { list-style: none; }
  .card-list li { position: relative; padding-left: 12px; margin-bottom: 5px; }
  .card-list li::before {
    content: ""; position: absolute; left: 0; top: 5px; width: 4px; height: 4px; border-radius: 50%; background: var(--gold);
  }
  .read-more {
    position: absolute; left: 14px; top: 152px; height: 16px; padding: 0 7px;
    background: var(--brown-deep); color: var(--white); font-size: 7.2px; line-height: 16px; text-decoration: none;
  }

  .ethics-photo {
    position: absolute; left: 77px; top: 799px; width: 206px; height: 300px;
    background: linear-gradient(160deg, #cdbfa8 0%, #e8e2d8 45%, #2b2522 75%, #d9d2c6 100%);
  }
  .ethics-label {
    position: absolute; left: 14px; top: 181px;
    font-size: 31px; font-weight: 800; line-height: 27px; color: var(--gold); letter-spacing: .5px;
  }
  .benefits {
    position: absolute; left: 297px; top: 834px; list-style: none;
  }
  .benefits li {
    display: flex; align-items: center; height: 28px; font-size: 8.6px; color: var(--text);
  }
  .benefits svg { width: 6px; height: 8px; margin-right: 14px; flex-shrink: 0; }

  .site-footer {
    position: absolute; left: 0; top: 1128px; width: 769px; height: 72px; background: var(--brown-deep);
  }
  .footer-nav {
    position: absolute; left: 76px; top: 22px; display: flex; align-items: center;
    font-size: 8.6px; font-weight: 600;
  }
  .footer-nav a { color: var(--white); text-decoration: none; }
  .footer-nav .sep { color: var(--white); margin: 0 11px; }
  .copyright {
    position: absolute; left: 76px; top: 45px; font-size: 8.6px; font-weight: 600; color: var(--white);
  }
  .social-circle {
    position: absolute; left: 673px; top: 27px; width: 18px; height: 18px; border-radius: 50%;
    border: 1px solid var(--white);
  }
</style>
</head>
<body>
  <header>
    <div class="hero-backdrop" role="img" aria-label="City skyline by the water in grey tones"></div>
    <nav class="nav-bar nav-bar--left">
      <a href="#">HOME</a><a href="#">ABOUT US</a><a href="#">SERVICES</a><a href="#">TEAM</a>
    </nav>
    <div class="brand"><span class="brand-name">Velvanta Staffing Co.</span></div>
    <nav class="nav-bar nav-bar--right">
      <a href="#">LOCATIONS</a><a href="#">TESTIMONIALS</a><a href="#">CONTACT US</a>
    </nav>
    <div class="hero-slide" role="img" aria-label="Three housekeepers in black uniforms standing in a hotel room"></div>
    <div class="slide-dots"><span class="is-active"></span><span></span><span></span><span></span></div>
  </header>

  <main>
    <h2 class="section-title team-title">TEAM</h2>
    <p class="team-intro">More than 300+ cleaning staff from Philippines, Nepal, Kenya &amp; Bangladesh; all experienced female cleaning staff possessing hospitable quality and pleasant in nature.All of our cleaners are insured and bonded; therefore you don't need to worry about the safety and security of your place. As we are locally owned and operated under British management, you can depend on our responsiveness, accountability and personal attention. When we clean your place, you get the perfect combination of professional quality and personal attention.</p>

    <h2 class="section-title training-title">OUR TRAINING PROGRAM</h2>

    <article class="program-card card-a">
      <h3 class="card-head">On Arrival of maids</h3>
      <p class="card-body">No matter how well or experienced cleaners we have; but we ensure Comprehensive QMS Cleaning Training provided on arrival. This is to make sure that the cleaners have complete know-how about cleaning, dealing with clients, etiquette and adapting with Doha environment.</p>
      <a class="read-more" href="#">Read More</a>
    </article>
    <article class="program-card card-b">
      <h3 class="card-head">We provide trainings on</h3>
      <div class="card-body">
        <ul class="card-list">
          <li>Service Industry - Hospitality</li>
          <li>Quality Cleaning Service Ironing</li>
          <li>Laundry Service/Usage of Washing machine</li>
          <li>Client's Property Safety</li>
          <li>Usage of Cleaning materials</li>
        </ul>
      </div>
      <a class="read-more" href="#">Read More</a>
    </article>
    <article class="program-card card-c">
      <h3 class="card-head">Refresher Course</h3>
      <p class="card-body">Quarterly refresher training is conducted for existing cleaners to ensure consistency of our service and upgrade maid's knowledge on the latest cleaning household materials/equipment.</p>
      <a class="read-more" href="#">Read More</a>
    </article>

    <div class="ethics-photo" role="img" aria-label="Smiling housekeeper in apron holding folded white towels">
      <span class="ethics-label">ETHICAL<br>TREATMENT</span>
    </div>
    <ul class="benefits">
      <li><svg viewBox="0 0 6 8"><path d="M1 1l3.5 3L1 7" fill="none" stroke="#d9a21b" stroke-width="1.4"/></svg>Bonus Scheme after 180 hours crossed in any month</li>
      <li><svg viewBox="0 0 6 8"><path d="M1 1l3.5 3L1 7" fill="none" stroke="#d9a21b" stroke-width="1.4"/></svg>Extra Bonus Scheme after 200 hours crossed in any month</li>
      <li><svg viewBox="0 0 6 8"><path d="M1 1l3.5 3L1 7" fill="none" stroke="#d9a21b" stroke-width="1.4"/></svg>OT payment 2.5 times [which is more than Regional Labor Office stated]</li>
      <li><svg viewBox="0 0 6 8"><path d="M1 1l3.5 3L1 7" fill="none" stroke="#d9a21b" stroke-width="1.4"/></svg>Medical Treatment Support</li>
      <li><svg viewBox="0 0 6 8"><path d="M1 1l3.5 3L1 7" fill="none" stroke="#d9a21b" stroke-width="1.4"/></svg>Awards [Employee of the month, Star of the Year etc..; and cash recognition]</li>
      <li><svg viewBox="0 0 6 8"><path d="M1 1l3.5 3L1 7" fill="none" stroke="#d9a21b" stroke-width="1.4"/></svg>Family Support</li>
      <li><svg viewBox="0 0 6 8"><path d="M1 1l3.5 3L1 7" fill="none" stroke="#d9a21b" stroke-width="1.4"/></svg>Birthday Gifts</li>
      <li><svg viewBox="0 0 6 8"><path d="M1 1l3.5 3L1 7" fill="none" stroke="#d9a21b" stroke-width="1.4"/></svg>Annual Party</li>
      <li><svg viewBox="0 0 6 8"><path d="M1 1l3.5 3L1 7" fill="none" stroke="#d9a21b" stroke-width="1.4"/></svg>Promotion Schemes</li>
      <li><svg viewBox="0 0 6 8"><path d="M1 1l3.5 3L1 7" fill="none" stroke="#d9a21b" stroke-width="1.4"/></svg>Salary Increment every year</li>
    </ul>
  </main>

  <footer class="site-footer">
    <nav class="footer-nav">
      <a href="#">Home</a><span class="sep">|</span>
      <a href="#">About Us</a><span class="sep">|</span>
      <a href="#">Services</a><span class="sep">|</span>
      <a href="#">Jobs</a><span class="sep">|</span>
      <a href="#">Maids</a><span class="sep">|</span>
      <a href="#">FAQ's</a><span class="sep">|</span>
      <a href="#">Testimonials</a><span class="sep">|</span>
      <a href="#">Contact Us</a>
    </nav>
    <p class="copyright">© 2014 Company Name ,All&nbsp; Rights Reserved</p>
    <span class="social-circle" aria-label="Social media link"></span>
  </footer>
</body>
</html>
```